life science staff augmentation business - website

We are looking to build a new website for a consulting business in life science industry. This business is to provide contracting/staff augmentation solution for the medical device/pharmaceutical/biopharmaceutical companies. We will provide recruiting solution, contract staffing solution and consulting solution to this industry. This should be about 5-6 page website. We already have the basics that we would like to see in this website but need help with the design, flow, picture and flash. Need a page with everyday new update that we wil gather from out side website. project to be completed asap.
Updates

Target Market(s)

Pharmaceutical and medical device companies. Providing staff augmentation service.
Examples:

www.corvenlo.example
www.tulbrix.example
www.quonselt.example

Industry/Entity Type

Medical

Requirements
Must have
• Home page with 3-4 rotating pictures. About us page, services page, industries served page, career page and contact us page. Each page to have some details. Not more than 15-20 lines on each page. Keep the same rotating image on all the pages. Home page to have feed from couple of government website news.
Nice to have
• website feel should be more towards pharma and med device industry. rotating logo on each page with mission statement running on the top of each page.
Should not have
• not to jazzy or many bright colors. simple but elegant in look. no facebook, twitter buttons. colorful background.

```html
<!DOCTYPE html>
<html lang="en">
<head>
<meta charset="utf-8">
<title>Life Science Staffing</title>
<link href="https://fonts.googleapis.com/css2?family=Raleway:wght@300;400;500;600;700&family=Noto+Serif&display=swap" rel="stylesheet">
<style>
:root{
  --blue:#2a8fd4;
  --logo:#3d7fc4;
  --ink:#333;
  --muted:#777;
  --faint:#aaa;
  --line:#e4e4e4;
  --quote-bg:#f1f3f5;
  --footer:#232323;
  --footer-deep:#1c1c1c;
  --footer-text:#8a8a8a;
  --green:#4a9e3c;
}
*{margin:0;padding:0;box-sizing:border-box}
html,body{width:698px;height:1200px;overflow:hidden;background:#fff}
body{position:relative;font-family:"Raleway",sans-serif;color:var(--ink)}
.abs{position:absolute}
.topbar{left:24px;top:8px;font-size:5.5px;letter-spacing:.5px;color:var(--faint)}
.topbar span{margin:0 3px}
.header-line{left:0;top:24px;width:698px;border-top:1px solid #f0f0f0}
.logo{left:24px;top:29px;font-size:18px;font-weight:300;color:var(--logo);letter-spacing:.5px}
.nav{top:39px;font-size:7.5px;letter-spacing:.5px;color:#444;font-weight:500}
.nav.active{color:var(--blue)}
.nav-active-bar{left:228px;top:23px;width:38px;height:2px;background:var(--blue)}
.hero{left:0;top:64px;width:698px;height:176px;background:linear-gradient(100deg,#b7d3ee 0%,#3b79bf 40%,#1d4f94 60%,#8fb6e0 100%)}
.dots{left:307px;top:228px;display:flex;gap:6px}
.dots i{display:block;width:5px;height:5px;border-radius:50%;background:#fff;opacity:.85}
.col-title{font-size:15px;font-weight:400;color:#222}
.body-text{font-size:7.3px;line-height:10.2px;color:var(--muted);letter-spacing:.6px}
.more{font-size:7.5px;color:var(--blue);letter-spacing:.5px}
.rule{border-top:1px solid var(--line)}
.photo-pills{background:linear-gradient(135deg,#f4a35a,#f7dcc5 55%,#e07585)}
.photo-lab{background:linear-gradient(135deg,#bcd0e0,#eef2f5 60%,#9fb8cc)}
.photo-tech{background:linear-gradient(90deg,#dbe9f5,#3c78b0 60%,#1a3550)}
.photo-caps{background:radial-gradient(circle at 50% 50%,#3b7fd0,#cfe0f2 55%,#fff 75%)}
.news-title{font-size:10.5px;color:#444;letter-spacing:.6px}
.news-date{font-size:6.5px;color:var(--faint);letter-spacing:.6px}
.feature-list{list-style:none;left:24px;top:527px;width:104px}
.feature-list li{position:relative;padding-left:13px;font-size:6.5px;line-height:6.8px;color:var(--muted);margin-bottom:6.5px;letter-spacing:.5px}
.feature-list svg{position:absolute;left:0;top:0}
.monitor{border:3px solid #2c2c2c;border-radius:2px}
.monitor-screen{width:100%;height:100%;background:linear-gradient(135deg,#c8d8e8,#8fa8c0)}
.monitor-stand{height:5px;background:linear-gradient(#dcdcdc,#b8b8b8);border-radius:0 0 4px 4px}
.section-label{font-size:8px;font-weight:700;letter-spacing:.6px;color:#222}
.quote-box{left:24px;top:882px;width:651px;height:62px;background:var(--quote-bg)}
.quote-text{left:16px;top:14px;font-family:"Noto Serif",serif;font-size:11px;line-height:17px;color:#666;letter-spacing:.5px;white-space:nowrap}
.avatar{left:24px;top:950px;width:62px;height:42px;border-radius:50%;background:linear-gradient(135deg,#d9d9d9,#7a7a7a)}
.footer{left:0;top:1012px;width:698px;height:148px;background:var(--footer)}
.footer-bottom{left:0;top:1160px;width:698px;height:40px;background:var(--footer-deep);border-top:1px solid #333}
.foot-head{font-size:6.8px;font-weight:700;letter-spacing:.6px;color:#ccc}
.foot-rule{border-top:1px solid #3a3a3a}
.foot-line{font-size:7.3px;color:var(--footer-text);letter-spacing:.6px;line-height:9px}
.foot-line b{color:#aaa;font-weight:600}
.copyright{left:26px;top:1177px;font-size:6px;color:#555;letter-spacing:.5px}
</style>
</head>
<body>

<div class="abs topbar">FORM<span>|</span>TERMS<span>|</span>CONTACT</div>
<div class="abs header-line"></div>
<div class="abs nav-active-bar"></div>
<div class="abs logo">YOUR LOGO</div>
<div class="abs nav active" style="left:233px">HOME</div>
<div class="abs nav" style="left:292px">ABOUT US</div>
<div class="abs nav" style="left:372px">SERVICES</div>
<div class="abs nav" style="left:451px">INDUSTRIES</div>
<div class="abs nav" style="left:539px">CARRIER</div>
<div class="abs nav" style="left:613px">CONTACT</div>
<div class="abs rule" style="left:0;top:62px;width:698px"></div>

<div class="abs hero" role="img" aria-label="Rotating banner: scientist in a laboratory holding a test tube beside glass flasks"></div>
<div class="abs dots"><i></i><i></i><i></i><i></i><i></i><i></i></div>

<div class="abs" style="left:27px;top:259px;width:182px">
  <h2 class="col-title">About Us</h2>
  <p class="body-text" style="margin-top:5px">Innovative design always develops in tandem with innovative technology, and can never be an end in itself. Lorem ipsum dolor</p>
  <p class="more" style="margin-top:6px">Learn more ›</p>
</div>
<div class="abs" style="left:253px;top:259px;width:182px">
  <h2 class="col-title">Our Services</h2>
  <p class="body-text" style="margin-top:5px">Innovative design always develops in tandem with innovative technology, and can never be an end in itself. Lorem ipsum dolor</p>
  <p class="more" style="margin-top:6px">Learn more ›</p>
</div>
<div class="abs" style="left:479px;top:259px;width:182px">
  <h2 class="col-title">Clients</h2>
  <p class="body-text" style="margin-top:5px">Innovative design always develops in tandem with innovative technology, and can never be an end in itself. Lorem ipsum dolor</p>
  <p class="more" style="margin-top:6px">Learn more ›</p>
</div>
<div class="abs rule" style="left:24px;top:367px;width:651px"></div>

<div class="abs" style="left:24px;top:383px;width:120px">
  <h2 class="col-title">Latest News</h2>
  <p class="body-text" style="font-size:6.8px;margin-top:5px;width:96px">Lorem ipsum dolor sit amet, consectetur adipiscing elit Aenean nisl orci</p>
  <p class="more" style="font-size:6.8px;margin-top:6px">See All ›</p>
</div>
<div class="abs rule" style="left:24px;top:474px;width:110px"></div>
<div class="abs col-title" style="left:24px;top:490px;width:112px;font-size:10.5px;line-height:13px;letter-spacing:.4px">&nbsp;&nbsp;&nbsp;&nbsp;&nbsp;Why Choose<br>Us?</div>
<ul class="abs feature-list">
  <li><svg width="7" height="6" viewBox="0 0 7 6"><path d="M1 3l2 2 3-4" fill="none" stroke="var(--green)" stroke-width="1.2"/></svg>Clean and User friendly layouts</li>
  <li><svg width="7" height="6" viewBox="0 0 7 6"><path d="M1 3l2 2 3-4" fill="none" stroke="var(--green)" stroke-width="1.2"/></svg>100% responsive layout and retina display ready</li>
  <li><svg width="7" height="6" viewBox="0 0 7 6"><path d="M1 3l2 2 3-4" fill="none" stroke="var(--green)" stroke-width="1.2"/></svg>Great quantity of high end features</li>
  <li><svg width="7" height="6" viewBox="0 0 7 6"><path d="M1 3l2 2 3-4" fill="none" stroke="var(--green)" stroke-width="1.2"/></svg>Well Organized and Great Documentations</li>
  <li><svg width="7" height="6" viewBox="0 0 7 6"><path d="M1 3l2 2 3-4" fill="none" stroke="var(--green)" stroke-width="1.2"/></svg>1200+ Font icons Integration</li>
  <li><svg width="7" height="6" viewBox="0 0 7 6"><path d="M1 3l2 2 3-4" fill="none" stroke="var(--green)" stroke-width="1.2"/></svg>Easy to Customize</li>
</ul>

<div class="abs photo-pills" style="left:190px;top:383px;width:235px;height:104px" role="img" aria-label="Spilled pills and tablets beside orange pill bottles"></div>
<div class="abs news-title" style="left:190px;top:496px">Save the World</div>
<div class="abs news-date" style="left:190px;top:513px">10 MAY 2013</div>

<div class="abs photo-lab" style="left:439px;top:383px;width:236px;height:105px" role="img" aria-label="Researchers in lab coats working with glassware"></div>
<div class="abs news-title" style="left:440px;top:497px">Mall Admirer</div>
<div class="abs news-date" style="left:440px;top:514px">10 MAY 2013</div>

<div class="abs photo-tech" style="left:190px;top:543px;width:235px;height:92px" role="img" aria-label="Business person touching a screen of digital interface icons"></div>
<div class="abs news-title" style="left:190px;top:643px">Spoilt for choice</div>
<div class="abs news-date" style="left:190px;top:661px">10 MAY 2013</div>

<div class="abs photo-caps" style="left:492px;top:548px;width:128px;height:72px" role="img" aria-label="Open capsule spilling small blue spheres"></div>
<div class="abs news-title" style="left:440px;top:636px">Busy girl</div>
<div class="abs news-date" style="left:440px;top:653px">10 MAY 2013</div>

<div class="abs" style="left:24px;top:706px;width:651px;border-top:1px dashed #e2e2e2"></div>

<div class="abs" style="left:24px;top:728px;width:182px">
  <h3 class="col-title" style="font-size:11.5px;width:220px;letter-spacing:.5px">Only Use what is necessary</h3>
  <p class="body-text" style="font-size:7px;margin-top:5px">Aliquam enim enim, pharetra in sodales at, interdum sit amet dui. Nullam vulputate euismod urna non pharetra. Phasellus blandit mattis ipsum, ac laoreet lorem lacinia et. Cras et ligula libero.</p>
  <p class="more" style="font-size:7px;margin-top:8px;width:200px">Haretra in sodales atsen interdum ›</p>
</div>
<div class="abs monitor" style="left:220px;top:748px;width:106px;height:50px"><div class="monitor-screen" role="img" aria-label="Team meeting in an office"></div></div>
<div class="abs monitor-stand" style="left:228px;top:798px;width:90px"></div>

<div class="abs" style="left:350px;top:728px;height:100px;border-left:1px solid var(--line)"></div>

<div class="abs" style="left:378px;top:728px;width:162px">
  <h3 class="col-title" style="font-size:11.5px;width:240px;letter-spacing:.5px">Clean and User friendly layouts</h3>
  <p class="body-text" style="font-size:7px;margin-top:5px">Aliquam enim enim, pharetra in sodales at, interdum sit amet dui. Nullam vulputate euismod urna non pharetra. Phasellus blandit mattis ipsum, ac laoreet lorem lacinia et. Cras et ligula</p>
  <p class="more" style="font-size:7px;margin-top:8px;width:200px">Haretra in sodales atsen interdum ›</p>
</div>
<div class="abs monitor" style="left:552px;top:748px;width:106px;height:50px"><div class="monitor-screen" role="img" aria-label="Group of colleagues seated at a table"></div></div>
<div class="abs monitor-stand" style="left:560px;top:798px;width:90px"></div>

<div class="abs section-label" style="left:24px;top:857px">WHAT OUR CLIENTS SAY</div>
<div class="abs rule" style="left:24px;top:872px;width:651px"></div>
<div class="abs quote-box">
  <p class="abs quote-text">Excellent design.I really love the designs of Daniel Orrin. He is indeed a great designer.<br>Everytime he amazed me with his great ideas.</p>
</div>
<svg class="abs" style="left:96px;top:943px" width="12" height="8" viewBox="0 0 12 8"><path d="M0 0h12L2 8z" fill="var(--quote-bg)"/></svg>
<div class="abs avatar" role="img" aria-label="Portrait photo of the client"></div>
<div class="abs" style="left:99px;top:961px;font-size:9px;font-weight:600;letter-spacing:.6px;color:#333">John Smith</div>
<div class="abs" style="left:99px;top:974px;font-size:7px;color:var(--muted);letter-spacing:.5px">Manager at Marlow Trading</div>

<div class="abs footer"></div>
<div class="abs foot-head" style="left:73px;top:1039px">CONTACT INFORMATION</div>
<div class="abs foot-head" style="left:320px;top:1039px">OUR CLIENTS</div>
<div class="abs foot-head" style="left:548px;top:1039px">ABOUT US</div>
<div class="abs foot-rule" style="left:24px;top:1052px;width:207px"></div>
<div class="abs foot-rule" style="left:246px;top:1052px;width:207px"></div>
<div class="abs foot-rule" style="left:468px;top:1052px;width:207px"></div>
<div class="abs" style="left:70px;top:1058px;width:130px;height:28px;background:radial-gradient(ellipse,#333 0%,transparent 70%)" role="img" aria-label="Faint world map decoration"></div>
<div class="abs foot-line" style="left:24px;top:1073px"><b>Address:</b> No.14 - 20415 Harlow Lane<br>City, Country</div>
<div class="abs foot-line" style="left:24px;top:1096px"><b>Phone:</b> + 1 (555) 014 2297</div>
<div class="abs foot-line" style="left:24px;top:1109px"><b>Fax:</b> + 1 (555) 014 2298</div>
<div class="abs foot-line" style="left:24px;top:1123px"><b>Email:</b> hello@tulvane.example</div>
<div class="abs footer-bottom"></div>
<div class="abs copyright">© 2012. All Rights Reserved. Powered By</div>

</body>
</html>
```